7Q - Quorvane Meridel Partners

We need a website designed for a new company based in the UAE. 7Q is a business consultancy training company aiming to provide strategic and sustainable solutions for their people and offer human development. The company offers research based consultancy.

Target Market(s)

Companies

Industry/Entity Type

Business Consultant

Number of Pages Required

2 page

Font styles to use
Other font styles liked:
• Century Gothic

Requirements
Must have
• Please look at other consultancy companies and make sure we have the main things on it.

```html
<!DOCTYPE html>
<html lang="en">
<head>
<meta charset="utf-8">
<title>Quorvane Meridel Partners</title>
<link href="https://fonts.googleapis.com/css2?family=Questrial&family=Jost:wght@400&display=swap" rel="stylesheet">
<style>
:root{
  --red:#9b0a1f;
  --red-icon:#a80d22;
  --ink:#1a1a1a;
  --muted:#555;
  --white:#fff;
  --footer:#151515;
}
*{box-sizing:border-box;margin:0;padding:0}
html,body{width:696px;height:1200px;overflow:hidden;background:var(--white)}
body{font-family:"Questrial",sans-serif;color:var(--ink);position:relative}
.abs{position:absolute}

/* header */
.site-header{left:0;top:0;width:696px;height:48px;background:var(--white)}
.brand{left:83px;top:9px;display:flex;align-items:center;gap:5px}
.brand-mark{width:22px;height:30px;border:1.5px solid var(--ink);border-radius:50%;display:flex;align-items:center;justify-content:center;font-size:11px}
.brand-name{font-size:10.5px;line-height:12px}
.main-nav{left:338px;top:19px;display:flex;font-size:9.5px}
.main-nav a{color:var(--ink);text-decoration:none;margin-right:24px}
.main-nav a.active{color:var(--red)}

/* hero */
.hero{left:0;top:48px;width:696px;height:332px;
  background:linear-gradient(90deg,#b9bfc5 0%,#dfe3e7 35%,#eef1f4 60%,#c9cdd2 85%,#a9adb3 100%)}
.hero-title{left:452px;top:211px;font-family:"Jost",sans-serif;font-weight:400;font-size:29px;line-height:34px;color:#111;letter-spacing:.3px}
.hero-title .accent{color:var(--red)}
.hero-dots{left:323px;top:357px;display:flex;gap:6px}
.hero-dots span{width:7.5px;height:7.5px;border-radius:50%;background:#d0d0d0}
.hero-dots span.on{background:#111}

/* intro band */
.intro{left:0;top:380px;width:696px;height:224px;background:var(--red);color:var(--white)}
.intro-photo{left:74px;top:35px;width:180px;height:144px;background:linear-gradient(120deg,#9a9a9a,#d8d8d8 55%,#8c8c8c)}
.intro-title{left:261px;top:33px;font-weight:400;font-size:15px;line-height:18.5px}
.intro-text{left:261px;top:77px;width:172px;font-size:6.6px;line-height:11.6px}
.news-title{left:449px;top:33px;font-weight:400;font-size:15px}
.news-item{left:449px;display:flex;gap:10px}
.news-date{width:27px;height:27px;background:#111;font-size:6.4px;line-height:7px;text-align:center;padding-top:3px}
.news-text{width:135px;font-size:6.5px;line-height:11.5px}
.news-text small{font-size:5.6px}

/* services */
.services-title{left:0;top:614px;width:696px;text-align:center;font-weight:400;font-size:15px;color:var(--red)}
.service{top:662px;width:120px;text-align:center}
.service-icon{width:34px;height:34px;border-radius:50%;background:var(--red-icon);margin:0 auto;display:flex;align-items:center;justify-content:center}
.service h3{font-weight:400;font-size:15px;margin-top:6px;color:#222}
.service p{font-size:6.8px;line-height:11.6px;color:var(--muted);margin-top:4px}

/* testimonials */
.testimonials{left:0;top:822px;width:696px;height:200px;background:linear-gradient(180deg,#2a2c31 0%,#1e2024 60%,#3a3029 100%);color:var(--white);text-align:center}
.testi-title{left:0;top:28px;width:696px;font-weight:400;font-size:14.5px}
.quote-mark{left:74px;top:64px;font-family:"Jost",sans-serif;font-size:26px;line-height:20px}
.testi-text{left:106px;top:80px;width:516px;font-size:6.6px;line-height:14.4px}
.testi-name{left:0;top:135px;width:696px;font-size:17px}
.testi-role{left:0;top:161px;width:696px;font-size:8.5px}
.arrow{top:94px;font-size:11px}

/* press */
.press{left:0;top:1022px;width:696px;height:68px;display:flex;align-items:center;justify-content:center;gap:18px;color:#555;font-size:8.5px}
.press span{white-space:nowrap}

/* footer */
.site-footer{left:0;top:1090px;width:696px;height:110px;background:var(--footer);color:var(--white);text-align:center}
.social{left:303px;top:19px;display:flex;gap:4.5px}
.social span{width:14.5px;height:14.5px;border-radius:50%;background:#8b8b8b}
.foot-nav{left:0;top:43px;width:696px;font-size:9px}
.foot-nav a{color:var(--white);text-decoration:none}
.foot-nav i{font-style:normal;margin:0 13px}
.copyright{left:0;top:64px;width:696px;font-size:8.8px}
</style>
</head>
<body>

<header class="site-header abs">
  <div class="brand abs"><div class="brand-mark">7Q</div><div class="brand-name">Quorvane<br>Meridel<br>Partners</div></div>
  <nav class="main-nav abs">
    <a class="active" href="#">Home</a><a href="#">About Us</a><a href="#">What We Do</a><a href="#">Team</a><a href="#">Contact</a>
  </nav>
</header>

<section class="hero abs" role="img" aria-label="Photo of a consultant in a suit with colleagues meeting in a bright office"></section>
<h1 class="hero-title abs">QUORVANE<br><span class="accent">MERIDEL</span><br>PARTNERS</h1>
<div class="hero-dots abs"><span class="on"></span><span></span><span></span><span></span></div>

<section class="intro abs">
  <div class="intro-photo abs" role="img" aria-label="Black and white photo of a business team seated at a meeting"></div>
  <h2 class="intro-title abs">Welcome to Quorvane<br>Meridel Partners</h2>
  <p class="intro-text abs">Lorem Ipsum is simply dummy text of the printing and typesetting industry. Lorem Ipsum has been the industry's standard dummy text ever since the 1500s, when an unknown printer took a galley of type and scrambled it to make a type specimen book. It has survived not only five centuries, but also the leap into electronic typesetting, remaining essentially unchanged. It was popularised in the 1960s with the release of Letraset sheets</p>
  <h2 class="news-title abs">Latest News</h2>
  <div class="news-item abs" style="top:73px">
    <div class="news-date">June<br>6th<br>2015</div>
    <p class="news-text">Lorem Ipsum is simply dummy text of the printing and typesetting industry.<br><small>Lorem Ipsum has been the industry's standard dummy text ever since the 1500s</small></p>
  </div>
  <div class="news-item abs" style="top:131px">
    <div class="news-date">June<br>6th<br>2015</div>
    <p class="news-text">Lorem Ipsum is simply dummy text of the printing and typesetting industry.<br><small>Lorem Ipsum has been the industry's standard dummy text ever since the 1500s</small></p>
  </div>
</section>

<h2 class="services-title abs">Our Services</h2>
<div class="service abs" style="left:77px">
  <div class="service-icon"><svg width="12" height="12" viewBox="0 0 12 12"><circle cx="5" cy="5" r="3.3" fill="none" stroke="#fff" stroke-width="1.6"/><line x1="7.5" y1="7.5" x2="10.5" y2="10.5" stroke="#fff" stroke-width="1.8"/></svg></div>
  <h3>Research</h3>
  <p>Lorem Ipsum is simply dummy text of the printing and typesetting industry.Lorem Ipsum has been the industry's standard dummy text ever since the 1500s</p>
</div>
<div class="service abs" style="left:225px">
  <div class="service-icon"><svg width="12" height="12" viewBox="0 0 12 12"><rect x="2" y="4" width="6" height="6" fill="#fff"/><circle cx="5" cy="3.5" r="1.6" fill="#fff"/><circle cx="8.5" cy="7" r="1.6" fill="#fff"/></svg></div>
  <h3>Integrity</h3>
  <p>Lorem Ipsum is simply dummy text of the printing and typesetting industry.Lorem Ipsum has been the industry's standard dummy text ever since the 1500s</p>
</div>
<div class="service abs" style="left:358px">
  <div class="service-icon"><svg width="12" height="12" viewBox="0 0 12 12"><circle cx="6" cy="6" r="4.5" fill="none" stroke="#fff" stroke-width="1.4"/><ellipse cx="6" cy="6" rx="2" ry="4.5" fill="none" stroke="#fff" stroke-width="1"/><line x1="1.5" y1="6" x2="10.5" y2="6" stroke="#fff" stroke-width="1"/></svg></div>
  <h3>Global</h3>
  <p>Lorem Ipsum is simply dummy text of the printing and typesetting industry.Lorem Ipsum has been the industry's standard dummy text ever since the 1500s</p>
</div>
<div class="service abs" style="left:499px">
  <div class="service-icon"><svg width="14" height="12" viewBox="0 0 14 12"><circle cx="7" cy="3.5" r="2" fill="#fff"/><circle cx="3" cy="4.5" r="1.5" fill="#fff"/><circle cx="11" cy="4.5" r="1.5" fill="#fff"/><rect x="4" y="6.5" width="6" height="4" rx="1.5" fill="#fff"/><rect x="0.5" y="7" width="4" height="3" rx="1.2" fill="#fff"/><rect x="9.5" y="7" width="4" height="3" rx="1.2" fill="#fff"/></svg></div>
  <h3>Consultancy</h3>
  <p>Lorem Ipsum is simply dummy text of the printing and typesetting industry.Lorem Ipsum has been the industry's standard dummy text ever since the 1500s</p>
</div>

<section class="testimonials abs" role="img" aria-label="Dusk city skyline with office towers behind the testimonial">
  <h2 class="testi-title abs">Testimonials</h2>
  <div class="quote-mark abs">&ldquo;</div>
  <p class="testi-text abs">Lorem Ipsum is simply dummy text of the printing and typesetting industry. Lorem Ipsum has been the industry's standard dummy text ever since the 1500s, when an unknown printer took a galley of type and scrambled it to make a type specimen book. It has survived not only five centuries, but also the leap into electronic typesetting, remaining essentially unchanged.</p>
  <div class="testi-name abs">Daniel Orrin</div>
  <div class="testi-role abs">Consultant Experts</div>
  <div class="arrow abs" style="left:41px">&lsaquo;</div>
  <div class="arrow abs" style="left:650px">&rsaquo;</div>
</section>

<section class="press abs">
  <span>Harbor Business Ledger</span><span>Tellmark</span><span>Veltora Network</span><span>Market Observer</span><span>Circuitwire</span><span>Westcoast Daily</span>
</section>

<footer class="site-footer abs">
  <div class="social abs"><span></span><span></span><span></span><span></span><span></span></div>
  <nav class="foot-nav abs"><a href="#">Home</a><i>|</i><a href="#">About Us</a><i>|</i><a href="#">What We Do</a><i>|</i><a href="#">Team</a><i>|</i><a href="#">Contact</a></nav>
  <p class="copyright abs">&copy; 2015 Company Name , All Rights Reserved</p>
</footer>

</body>
</html>
```